professional coaching community needs new look for website

We require a website design that attracts professionals. We run a large, global professional coaching community (e.g. executive, business, personal coaches NOT sports coaches). Our members are committed to their professional and personal development and they enjoy building relationships with other coaches across the world. We also champion the success of coaches and the coaching industry by providing business support resources to our members. We do not mind which colours you use, but whatever the combination, the combinations must be professional and refined. It would be good to have some of the familiarity of the old site colours, with some new, more professional element. We have a number of requirements for the homepage and members design, and this is attached.

Reason: I am extending the deadline for this design, in order to give feedback and see how current designs can be tweaked.

Target Market(s)

Here are some ideas for images, which gives and idea of the target market also:

Ideas for website images:

1. http://www.pixelvarno.com/stock-photo-48213077-business-success.php?st=4b2a918 (I like the people in this one – they seem very dynamic and a good mix of women and men)
2. http://www.pixelvarno.com/stock-photo-51729406-business-communications.php?st=4b2a918 (I like all of the speech bubbles in this one, that’s what the MentraLoop community does – pairs up in two’s or small groups and engages in professional talking)
3. http://www.pixelvarno.com/stock-photo-37086152-global-business-working.php?st=4b2a918 (I like the combination of the world and the people talking in different groups)
4. http://www.pixelvarno.com/stock-photo-44861039-global-business-people.php?st=e512604 (I like the world in this one – would be good to see combination of world and #1 dynamic people, which is the MentraLoop community)

Industry/Entity Type

Building

Requirements
Must have
• See attached uploaded files including homepage design, member dashboard design, and example profile (profiles need to be included him banner design). Note that any text must not be build into graphic. It needs to be able to be edited via html.

```html
<!DOCTYPE html>
<html lang="en">
<head>
<meta charset="utf-8">
<title>MentraLoop — Coaching Community</title>
<link rel="stylesheet" href="https://fonts.googleapis.com/css2?family=Lato:wght@400;700&family=Open+Sans:wght@400;600;700&display=swap">
<style>
:root{
  --navy:#1f3f73;
  --brand-blue:#1d4f8a;
  --link-teal:#2a7b8f;
  --green:#6cb56a;
  --green-dark:#4f9a4d;
  --text:#222;
  --muted:#666;
  --panel-border:#d4d4d4;
  --footer:#3b3b3b;
  --footer-bottom:#2c2c2c;
  --footer-text:#9a9a9a;
  --button:#1f3a66;
}
*{box-sizing:border-box;margin:0;padding:0}
html,body{width:895px;height:1200px;overflow:hidden}
body{position:relative;background:#fff;font-family:"Open Sans",Arial,sans-serif;color:var(--text);font-size:11px}
.abs{position:absolute}

/* header */
.site-header{left:0;top:0;width:895px;height:48px;background:linear-gradient(#fff,#f1f1f1);border-bottom:1px solid #ddd;z-index:2}
.brand{left:101px;top:9px;font-family:"Lato",sans-serif;font-weight:700;font-size:24px;color:var(--brand-blue);letter-spacing:-.3px}
.main-nav{left:405px;top:24px;display:flex;gap:0;font-size:11.5px;color:#333}
.main-nav span{margin-right:17px}
.lang{left:713px;top:0;width:72px;height:16px;background:#e3e3e3;border-radius:0 0 4px 4px;font-size:9px;color:#888;padding:2px 0 0 8px}
.lang i{display:inline-block;width:10px;height:7px;background:#c9d3e6;margin-right:4px;vertical-align:-1px}

/* hero */
.hero-photo{left:0;top:48px;width:895px;height:282px;background:radial-gradient(ellipse at 30% 40%,#e9f0fb 0%,#a9c0e6 35%,#5c7fbf 70%,#3d5e9c 100%)}
.hero-title{left:121px;top:158px;font-family:"Lato",sans-serif;font-weight:700;font-size:28px;line-height:34px;color:#111;letter-spacing:-.4px}
.login{left:572px;top:68px;width:212px;height:216px;background:rgba(214,228,248,.82);border:1px solid rgba(255,255,255,.7);border-radius:4px;box-shadow:0 1px 4px rgba(0,0,0,.15)}
.login h2{position:absolute;left:0;width:100%;top:19px;text-align:center;font-family:"Lato",sans-serif;font-weight:700;font-size:14px;color:var(--navy)}
.field-label{position:absolute;font-size:9.5px;color:#222}
.input{position:absolute;height:20px;background:#fff;border:1px solid #c4cfdf;border-radius:2px;font-size:8px;font-style:italic;color:#aaa;padding:4px 0 0 6px}
.check{position:absolute;width:10px;height:10px;background:#fff;border:1px solid #aab}
.btn{position:absolute;background:var(--button);color:#fff;font-size:10px;font-weight:600;text-align:center;border-radius:2px;line-height:18px}
.login .rule{position:absolute;left:11px;width:192px;top:173px;border-top:1px solid #b9c8df}
.login .foot{position:absolute;left:12px;top:179px;font-size:8.5px;line-height:13px;color:#333}
.login .foot a{color:var(--link-teal);text-decoration:none}

/* benefits */
.panel{background:#fff;border:1px solid var(--panel-border)}
.benefits{left:105px;top:347px;width:454px;height:130px}
.panel-head{height:28px;background:linear-gradient(#fff,#eee);border-bottom:1px solid var(--panel-border);text-align:center;font-family:"Lato",sans-serif;font-size:14px;color:var(--navy);line-height:28px}
.benefit-cols{display:flex;padding:19px 0 0 20px}
.benefit-cols ul{list-style:none;width:155px;font-family:"Lato",sans-serif;font-size:11.5px;line-height:21px}
.benefit-cols li::before{content:"•";color:var(--green-dark);margin-right:5px}

/* video */
.video{left:106px;top:491px;width:453px;height:290px;background:#0b0b0b}
.video .still{position:absolute;left:0;top:22px;width:453px;height:236px;background:radial-gradient(ellipse at 50% 55%,#6b665c 0%,#3b3833 40%,#111 80%)}
.video .title{position:absolute;left:7px;top:5px;font-size:9px;color:#eee}
.video .play{position:absolute;left:216px;top:137px}
.video .bar{position:absolute;left:0;top:266px;width:453px;height:4px;background:#555}
.video .bar b{display:block;width:96px;height:4px;background:#d00}
.video .knob{position:absolute;left:92px;top:263px;width:10px;height:10px;border-radius:50%;background:#ddd}
.video .ctrl{position:absolute;left:0;top:270px;width:453px;height:20px;background:#1c1c1c;font-size:8px;color:#ccc}

/* article */
.article{left:115px;top:808px;width:440px}
.article h3{font-family:"Lato",sans-serif;font-weight:400;font-size:14.5px;color:var(--navy);margin-bottom:8px}
.article p{font-size:10.4px;line-height:19.5px;color:#222}
.article a{color:var(--brand-blue);text-decoration:none}

/* quick sign-in */
.signin{left:573px;top:347px;width:211px;height:340px;background:linear-gradient(#e9f1fb,#d6e4f5);border:1px solid #d3dceb;border-radius:3px}
.ribbon{position:absolute;left:0;top:0;width:211px;height:36px;background:linear-gradient(#86c783,#5fae5c);color:#fff;font-family:"Lato",sans-serif;font-weight:700;font-size:15px;text-align:center;line-height:30px;clip-path:polygon(0 0,100% 0,100% 78%,50% 100%,0 78%)}
.perks{position:absolute;left:0;top:48px;list-style:none;font-size:9.6px;font-weight:600;color:#222}
.perks li{position:relative;padding-left:24px;line-height:10px;margin-bottom:0}
.perks li::before{content:"";position:absolute;left:0;top:1px;width:18px;height:12px;background:var(--green);clip-path:polygon(0 0,65% 0,100% 50%,65% 100%,0 100%)}
.signin .rule{position:absolute;left:8px;width:194px;top:178px;border-top:1px solid #b6c7de}
.signin .terms{position:absolute;left:24px;top:277px;font-size:8.5px;line-height:10px;color:var(--link-teal);width:170px}

.adv{left:573px;top:707px;width:211px;height:74px;background:#b9b9b9;color:#8a8a8a;font-family:"Lato",sans-serif;font-weight:700;font-size:13px;text-align:center;line-height:74px}
.social{left:576px;top:794px;display:flex;gap:7px}
.social i{display:block;width:20px;height:20px;border-radius:50%;background:#b5b5b5}
.social i.active{background:var(--green)}

.supporters{left:574px;top:825px;width:210px;height:251px}
.supporters .panel-head{text-align:left;padding-left:13px;height:32px;line-height:32px}
.sponsor{position:absolute;left:8px;width:194px;height:60px;border-bottom:1px solid #ddd;text-align:center;line-height:60px;font-family:"Lato",sans-serif;font-weight:700;font-size:14px}
.supporters .more{position:absolute;left:0;width:100%;top:232px;text-align:center;font-size:8.5px;color:#b02020}

/* footer */
.footer{left:0;top:1086px;width:895px;height:86px;background:var(--footer)}
.footer-notch{left:441px;top:1085px;width:14px;height:8px;background:#fff;clip-path:polygon(0 0,100% 0,50% 100%)}
.footer-nav{left:120px;top:1112px;font-size:7.5px;color:var(--footer-text);display:flex}
.footer-nav span{padding:0 14px;border-left:1px solid #555}
.footer-nav span:first-child{padding-left:0;border:0}
.footer-nav .current{color:var(--green)}
.footer .rule{position:absolute;left:120px;width:490px;top:42px;border-top:1px solid #4c4c4c}
.footer .rule2{position:absolute;left:623px;width:153px;top:42px;border-top:1px solid #4c4c4c}
.contact{left:120px;top:1138px;font-size:8px;color:var(--footer-text);display:flex;align-items:center}
.contact svg{margin-right:5px}
.contact span{margin-right:22px;display:flex;align-items:center}
.stay{left:623px;top:1112px;font-size:7.5px;color:var(--footer-text)}
.footer-icons{left:624px;top:1139px;display:flex;gap:11px}
.footer-icons i{display:block;width:13px;height:13px;border-radius:2px;background:#777}
.footer-icons i.active{background:var(--green)}
.footer-bottom{left:0;top:1172px;width:895px;height:28px;background:var(--footer-bottom);font-size:8px;color:var(--footer-text);padding:10px 0 0 119px}
.footer-bottom span{padding:0 8px;border-left:1px solid #555}
.footer-bottom span:first-child{padding-left:0;border:0}
</style>
</head>
<body>

<header class="site-header abs">
  <div class="brand abs">MentraLoop</div>
  <nav class="main-nav abs"><span>Home</span><span>Join Us</span><span>Coaching</span><span>Mentoring</span><span>Supervision</span><span>Resources</span></nav>
  <div class="lang abs"><i></i>English ⌄</div>
</header>

<div class="hero-photo abs" role="img" aria-label="Blue-toned photograph of chess pieces with a large king in the foreground"></div>
<h1 class="hero-title abs">Join the most dinamic coaching<br>community in the world</h1>

<form class="login abs">
  <h2>Login in MentraLoop</h2>
  <span class="field-label" style="left:10px;top:60px">Username:</span>
  <div class="input" style="left:61px;top:55px;width:139px">Your name</div>
  <span class="field-label" style="left:10px;top:91px">Password:</span>
  <div class="input" style="left:61px;top:87px;width:139px">Your name</div>
  <div class="check" style="left:60px;top:117px"></div>
  <span class="field-label" style="left:75px;top:117px;font-size:8.5px">Keep me logged in</span>
  <div class="btn" style="left:70px;top:141px;width:73px">Login</div>
  <div class="rule"></div>
  <p class="foot"><a href="#">Forged Password?</a><br>Not a MentraLoop yet? <a href="#">Register Now.</a></p>
</form>

<section class="benefits panel abs">
  <div class="panel-head">Why are there XXXX MentraLoops?</div>
  <div class="benefit-cols">
    <ul><li>Benefit 1</li><li>Benefit 2</li><li>Benefit 3</li></ul>
    <ul><li>Benefit 1</li><li>Benefit 2</li><li>Benefit 3</li></ul>
    <ul><li>Benefit 1</li><li>Benefit 2</li><li>Benefit 3</li></ul>
  </div>
</section>

<section class="video abs">
  <div class="still" role="img" aria-label="Video still of a white chess king on a dark chessboard"></div>
  <div class="title">2013 Streamly Player PSD</div>
  <svg class="play" width="22" height="22" viewBox="0 0 22 22"><path d="M5 3 L19 11 L5 19Z" fill="#fff"/></svg>
  <div class="bar"><b></b></div>
  <div class="knob"></div>
  <div class="ctrl">
    <svg style="position:absolute;left:15px;top:5px" width="10" height="10"><path d="M1 0 L10 5 L1 10Z" fill="#ccc"/></svg>
    <svg style="position:absolute;left:42px;top:5px" width="12" height="10"><path d="M0 3 H3 L7 0 V10 L3 7 H0Z" fill="#ccc"/></svg>
    <span style="position:absolute;left:63px;top:5px"><b style="color:#fff">0:42</b> / 3:20</span>
    <span style="position:absolute;left:394px;top:5px">Streamly</span>
    <svg style="position:absolute;left:431px;top:5px" width="11" height="11"><path d="M0 3V0H3M8 0H11V3M11 8V11H8M3 11H0V8" stroke="#ccc" fill="none" stroke-width="1.5"/></svg>
  </div>
</section>

<article class="article abs">
  <h3>Not Too Long Header</h3>
  <p>Lorem ipsum dolor sit amet, consectetuer adipiscing elit. Aenean commodo ligula eget dolor. Aenean massa. Cum sociis natoque penatibus et magnis dis parturient montes, nascetur ridiculus mus. Donec quam felis, ultricies nec, pellentesque eu, pretium quis, sem. Nulla consequat massa quis enim. Donec pede justo, fringilla vel, aliquet nec, vulputate eget, arcu. In enim justo, rhoncus ut, imperdiet a, venenatis vitae, justo. Nullam dictum felis eu pede mollis pretium. Integer tincidunt. Cras dapibus.<br><a href="#">Vivamus elementum semper nisi.</a> Aenean vulputate eleifend tellus. Aenean leo ligula, porttitor eu, consequat vitae, eleifend ac, enim. Aliquam lorem ante, dapibus in, viverra quis, feugiat a, tellus. Phasellus viverra nulla ut metus varius laoreet. Quisque rutrum. Aenean imperdiet. Etiam ultricies nisi vel augue. Curabitur ullamcorper ultricies nisi. Nam eget dui.</p>
</article>

<aside class="signin abs">
  <div class="ribbon">Quick Sign In</div>
  <ul class="perks">
    <li style="margin-top:2px">Free to join</li>
    <li style="margin-top:14px">3 issues of Coaching Research<br>in Practice</li>
    <li style="margin-top:14px">Monthly issues of Lessons from<br>the Field</li>
    <li style="margin-top:15px">Access to our community</li>
    <li style="margin-top:14px">Online profile</li>
  </ul>
  <div class="rule"></div>
  <span class="field-label" style="left:8px;top:193px">First Name:</span>
  <div class="input" style="left:63px;top:187px;width:139px">Your name</div>
  <span class="field-label" style="left:8px;top:223px">Last Name:</span>
  <div class="input" style="left:63px;top:218px;width:139px">Your name</div>
  <span class="field-label" style="left:8px;top:253px">Email:</span>
  <div class="input" style="left:63px;top:247px;width:139px">Your name</div>
  <div class="check" style="left:9px;top:276px"></div>
  <p class="terms">I have read the MentraLoop Terms and Conditions</p>
  <div class="btn" style="left:69px;top:306px;width:73px">Sign Up Now</div>
</aside>

<div class="adv abs">Adv</div>
<div class="social abs"><i></i><i class="active"></i><i></i><i></i></div>

<section class="supporters panel abs">
  <div class="panel-head">Thanks to our Supporters</div>
  <div class="sponsor" style="top:36px;color:#e8541e">Northvane</div>
  <div class="sponsor" style="top:98px;color:#1d2e5a">Corlith</div>
  <div class="sponsor" style="top:159px;color:#e8862a;border:0">Paylumen</div>
  <div class="more">See more of our supporters »</div>
</section>

<footer class="footer abs">
  <div class="rule"></div><div class="rule2"></div>
</footer>
<div class="footer-notch abs"></div>
<nav class="footer-nav abs"><span>HOME</span><span class="current">FEATURES</span><span>BLOG</span><span>PORTFOLIO</span><span>CONTACT</span></nav>
<div class="contact abs">
  <span><svg width="11" height="10"><path d="M0 5 L5.5 0 L11 5 H9 V10 H2 V5Z" fill="#888"/></svg>48 Harbor Lane. Lakeview, LV, 54321. USA</span>
  <span><svg width="10" height="10"><path d="M1 1 Q0 5 4 8.5 Q8 11 9 9 L7 6.5 L5.5 7.5 Q3 6 2.5 4.5 L3.5 3 Z" fill="#888"/></svg>(555) 210-4378</span>
  <span><svg width="11" height="8"><rect width="11" height="8" fill="#888"/><path d="M0 0 L5.5 4.5 L11 0" stroke="#3b3b3b" fill="none"/></svg>hello@mentraloop.example</span>
</div>
<div class="stay abs">STAY CONNECTED</div>
<div class="footer-icons abs"><i></i><i></i><i></i><i class="active"></i><i></i><i></i></div>
<div class="footer-bottom abs"><span>Mentra © 2013</span><span>Legal Notice</span><span>Terms</span></div>

</body>
</html>
```